Elegant brochure for BtoB Wine event in Asia

I need a design for a 4 pages brochure promoting 2 wine in Asia (China and Taiwan), A4 format. These 2 events will be open to professionals only. The hotel is located in the heart of Asia. The design has to show as well as the topic of these 2 wine, which is the wine. Colors can be black and red. The hotel is located in the heart of the city, in the heart of the city. ...
Target Market(s)
Wine industry. European wineries and Asian wine importers-distributors.
Industry/Entity Type
Events
Requirements
Must have
- Show the 2 main ideas: Wine and Asia High level, exclusivity, luxury atmosphere
Nice to have
- It would be great if page 3 and page 5 could be writable.

```html
<!DOCTYPE html>
<html lang="fr">
<head>
<meta charset="utf-8">
<title>European Wines Discovery Tour 2017 – Brochure</title>
<link rel="stylesheet" href="https://fonts.googleapis.com/css2?family=Oswald:wght@400;500;600;700&family=Open+Sans:wght@300;400;600;700&display=swap">
<style>
:root{
  --red:#e3101a;
  --dark:#262626;
  --ink:#222;
  --grey:#555;
  --line:#9a9a9a;
  --paper:#fff;
  --stage:#c98a4e;
  --label:#fff;
}
*{margin:0;padding:0;box-sizing:border-box}
html,body{width:1200px;height:1200px;overflow:hidden}
body{background:var(--stage);font-family:"Open Sans",Arial,sans-serif;color:var(--ink);position:relative}
.page{position:absolute;width:381px;height:540px;background:var(--paper);overflow:hidden;box-shadow:0 2px 6px rgba(0,0,0,.35)}
.p-cover{left:193px;top:21px;background:var(--dark)}
.p-one{left:626px;top:21px}
.p-two{left:193px;top:613px}
.p-back{left:626px;top:613px}
.page-label{position:absolute;width:381px;text-align:center;font-family:"Oswald",sans-serif;font-weight:500;font-size:18px;color:var(--label);letter-spacing:.5px}
.abs{position:absolute}
.red{color:var(--red)}
.foot-bar{position:absolute;left:0;right:0;bottom:0;height:10px;background:var(--red)}
.brand{display:flex;align-items:center;gap:4px;font-weight:700}
.brand .dot{border-radius:50%;background:var(--red);flex:none}

/* cover */
.cover-photo{left:0;top:0;width:381px;height:203px;background:linear-gradient(160deg,#5a4a3e,#2d2622 55%,#70625a)}
.cover-rule{left:0;top:203px;width:381px;height:3px;background:#ddd}
.cover-title{left:62px;top:224px;font-family:"Oswald",sans-serif;font-weight:500;color:var(--red);font-size:23px;line-height:25px}
.cover-year{left:228px;top:215px;font-family:"Oswald",sans-serif;font-weight:700;color:var(--red);font-size:58px;line-height:60px}
.cover-asia{left:62px;top:283px;width:312px;display:flex;align-items:center;gap:10px;color:#fff;font-family:"Oswald",sans-serif;font-size:17px;letter-spacing:5px}
.cover-asia span.rule{flex:1;height:2px;background:#fff}
.cover-cities{left:62px;top:312px;font-family:"Oswald",sans-serif;font-weight:600;color:#fff;font-size:34px}
.cover-date{left:64px;top:368px;width:254px;height:64px;border:2px solid #fff;border-radius:6px;background:var(--red);box-shadow:0 0 0 2px var(--red);color:#fff;text-align:center}
.cover-date b{display:block;font-family:"Oswald",sans-serif;font-weight:600;font-size:30px;line-height:36px;margin-top:3px}
.cover-date span{font-size:13.5px}
.cover-org{left:66px;top:456px;color:#fff;font-weight:300;font-size:23px;line-height:28px}
.cover-brand{left:255px;top:458px;color:#fff;font-size:13px;flex-direction:column;gap:2px;align-items:center}
.cover-brand .dot{width:34px;height:34px}

/* page one */
.head-band{left:0;top:0;width:381px;height:53px;background:var(--dark);color:#fff}
.head-band .brand{position:absolute;left:10px;top:12px;flex-direction:column;gap:1px;font-size:5px}
.head-band .brand .dot{width:18px;height:18px}
.head-title{position:absolute;left:62px;top:10px;font-family:"Oswald",sans-serif;font-size:15.5px;line-height:17px;font-weight:500}
.head-title small{display:block;text-align:right;font-size:13px}
.head-year{position:absolute;left:302px;top:6px;font-family:"Oswald",sans-serif;font-size:40px;font-weight:500;line-height:44px}
.body-txt{font-size:4.6px;line-height:6.1px;text-align:justify;color:var(--ink)}
.body-txt p{margin-bottom:3px}
.lead-txt{font-size:6.6px;line-height:8.6px;color:var(--ink)}
.red-strip{left:13px;top:164px;width:355px;height:14px;background:var(--red);color:#fff;font-size:6.6px;font-weight:700;text-align:center;line-height:14px}
.venue-box{left:13px;top:180px;width:355px;height:46px;border:1px solid var(--line);display:flex}
.venue-box div{flex:1;text-align:center;font-size:4.8px;line-height:7px;font-weight:600;padding-top:4px}
.venue-box div+div{border-left:1px solid var(--line)}
.section-head{display:flex;align-items:center;gap:6px;font-size:6.8px;font-weight:700;color:var(--ink)}
.section-head::before,.section-head::after{content:"";flex:1;height:1px;background:var(--ink)}
.section-head::before{flex:0 0 130px}

/* page two */
.form-txt{font-size:4.8px;line-height:6.6px;color:var(--ink)}
.form-txt b{font-weight:700}
.bullet{display:flex;gap:3px;align-items:flex-start}
.bullet i{flex:none;width:5px;height:5px;border:1px solid var(--red);border-radius:50%;margin-top:1px}
.reg-box{left:90px;top:113px;width:236px;height:44px;border:1.5px solid var(--red);border-radius:8px;background:#fff;text-align:center;padding-top:4px}
.reg-box b{display:block;font-family:"Oswald",sans-serif;font-weight:500;font-size:11px;line-height:14px}
.reg-box span{font-size:5.8px;font-weight:600;line-height:8px;display:block}
.reg-rule{left:13px;top:135px;width:355px;height:1px;background:var(--ink)}
.dotrow{display:flex;gap:2px;font-size:4.8px;line-height:9.5px}
.dotrow span.fill{flex:1;border-bottom:1px dotted #777;margin-bottom:2px}
.form-head{font-size:7px;font-weight:700;color:var(--red)}
table.grid{border-collapse:collapse;width:100%;font-size:4.6px;line-height:6px}
table.grid td{border:1px solid var(--line);padding:2px 3px;vertical-align:top}
table.grid td.c{text-align:center}
.box{display:inline-block;width:4px;height:4px;border:.6px solid #333;vertical-align:-0.5px;margin:0 1px}

/* back cover */
.sheet{left:13px;top:13px;width:355px;height:460px;border:1px solid #888;border-radius:8px}
.sheet-title{font-family:"Oswald",sans-serif;font-weight:400;font-size:9.5px;text-align:center;color:var(--ink)}
.fl{position:absolute;left:7px;right:7px;display:flex;gap:2px;font-size:4.6px;font-family:"Oswald",sans-serif;color:var(--ink)}
.fl span.fill{flex:1;border-bottom:1px dotted #777;margin-bottom:1px}
.sheet-mark{left:90px;top:170px;width:175px;height:175px;border-radius:50%;background:#f5f5f5}
.contact-head{left:0;top:486px;width:381px;text-align:center;font-family:"Oswald",sans-serif;font-size:11.5px;color:var(--ink)}
.contact-pill{left:13px;top:506px;width:355px;height:27px;border-radius:7px;background:var(--red);color:#fff;font-size:5px;text-align:center;padding-top:5px;line-height:8px}
.contact-pill b{font-weight:700}
.ico{display:inline-block;vertical-align:-1px;margin:0 2px}
</style>
</head>
<body>

<!-- FRONT COVER -->
<section class="page p-cover">
  <div class="abs cover-photo" role="img" aria-label="Photo d'une dégustation de vins : professionnels goûtant des vins à un stand"></div>
  <div class="abs cover-rule"></div>
  <div class="abs cover-title">European Wines<br>DISCOVERY TOUR</div>
  <div class="abs cover-year">2017</div>
  <div class="abs cover-asia"><span class="rule"></span>IN ASIA</div>
  <div class="abs cover-cities">Taipei &amp; Shenzhen</div>
  <div class="abs cover-date"><b>5 &amp; 7 DECEMBRE</b><span>400 wine professionals in 2 days</span></div>
  <div class="abs cover-org">Un evenement<br>ORGANISE PAR</div>
  <div class="abs brand cover-brand"><span class="dot"></span>Vineway Events</div>
  <div class="foot-bar" style="height:5px"></div>
</section>
<div class="page-label" style="left:193px;top:571px">FRONT COVER</div>

<!-- PAGE 1 -->
<section class="page p-one">
  <div class="abs head-band">
    <div class="brand"><span class="dot"></span>Vineway Events</div>
    <div class="head-title">EUROPEAN WINES DISCOVERY TOUR<small>in Asia</small></div>
    <div class="head-year">2017</div>
  </div>
  <div class="abs body-txt" style="left:13px;top:62px;width:355px">
    <p>Vous nous connaissez ou avez déjà bénéficié de nos services, sans le savoir.</p>
    <p>Une agence événementielle, avec une équipe expérimentée, bénéficiant d'une longue expérience dans l'organisation d'événements professionnels sur le marché asiatique. Travaillant très souvent dans l'ombre des principaux organisateurs, nous vous proposons aujourd'hui 2 événements professionnels pour une efficacité maximale.</p>
    <p>Nous souhaitons proposer aux producteurs de vins européens une alternative aux offres existantes, en leur apportant de la nouveauté à travers des bases de données mises à jour quotidiennement, sur des marchés où tout le monde suit l'évolution.</p>
    <p>A travers notre activité, nous connaissons l'ensemble de la filière, allant de l'importateur au distributeur jusqu'aux prescripteurs finaux, que sont les sommeliers et les F&amp;B entres autres.</p>
    <p>Pour en savoir plus sur nous : <span class="red">www.vineway-events.net</span></p>
    <p><b>Notre proposition – notre engagement</b></p>
  </div>
  <div class="abs red-strip">2 jours, 2 villes, 2 pays, combien de jours de prospection économisé pour vous ?</div>
  <div class="abs venue-box">
    <div><span class="red">TAIPEI, TAIWAN – GRAND PLAZA</span><br>On December 5th, 1pm-7pm<br>50 producteurs de vins européens<br>200 visiteurs professionnels</div>
    <div><span class="red">SHENZHEN, CHINA – RIVERSIDE HOTEL</span><br>On December 7th, 1pm-7pm<br>50 producteurs de vins européens<br>200 visiteurs professionnels</div>
  </div>
  <div class="abs section-head" style="left:13px;top:231px;width:355px">POURQUOI TAIPEI - TAIWAN ?</div>
  <div class="abs body-txt" style="left:13px;top:243px;width:171px">
    <p><span class="red">LE MARCHÉ :</span> Avec une population de plus de 23 millions, Taiwan est un marché important pour l'importation de boissons alcoolisées. Au cours des six dernières années, une augmentation annuelle de la consommation a été enregistrée, soit 8,6% pour le vin et 8,8% pour les spiritueux. Taiwan figure au nombre des 5 plus importants marchés pour le vin en Asie.</p>
    <p><span class="red">LES OPPORTUNITÉS :</span> Émergence de nouveaux groupes de consommateurs parmi les citadins et les femmes. Forte demande pour le vin en raison de l'augmentation du nombre de touristes en provenance de la Chine continentale. Des habitudes de consommation en pleine évolution avec l'arrivée de nouveaux consommateurs ayant déjà développé une préférence pour le vin.</p>
  </div>
  <div class="abs body-txt" style="left:197px;top:243px;width:171px">
    <p>Comme Taiwan n'est pas considéré comme un marché de volume, souvent à tort, il n'y aucune exposition vin majeure pour les professionnels, beaucoup de dégustations pour le grand public. Ce qui a pour conséquence de mobiliser les professionnels lorsqu'un événement est organisé, et d'être plutôt bien accueilli.</p>
    <p><span class="red">LE + :</span> Taiwan étant à proximité de sa grande sœur chinoise, et face à Xiamen, ville chinoise côtière particulièrement riche et dynamique, depuis que les relations en la Grande Chine et Taiwan se sont normalisées, avec l'ouverture de nouveau de lignes aériennes directes, de nombreux importateurs taiwanais ont ouvert un bureau à Xiamen pour leur développement sur le continent.</p>
  </div>
  <div class="abs lead-txt" style="left:13px;top:352px;width:355px">Vineway Events a déjà organisé un événement majeur à Taipei, qui a comptabilisé plus de 500 visiteurs professionnels</div>
  <div class="abs section-head" style="left:13px;top:385px;width:355px">POURQUOI SHENZHEN ?</div>
  <div class="abs body-txt" style="left:13px;top:397px;width:355px">
    <p><span class="red">LE MARCHÉ :</span> Situé en bordure de Hong Kong, en 1979 une partie de son territoire acquiert le statut de zone économique spéciale et devient l'un des principaux lieux d'expérimentation de la politique d'ouverture aux investissements étrangers. Bénéficiant de sa position géographique privilégiée, elle connaît un essor économique et démographique spectaculaire. Aujourd'hui elle compte environ 11 millions d'habitants et constitue une des municipalités les plus riches de Chine. Elle fait partie de la mégalopole chinoise du delta de la Rivière des Perles.</p>
    <p><span class="red">LES OPPORTUNITÉS :</span> La population de Shenzhen est jeune, aisée, et bénéficie de l'influence de sa voisine hongkongaise sur les modes de consommation. Le vin devient une boisson à la mode. C'est à Shenzhen que sont localisés tous les sièges sociaux des principales sociétés chinoises du numérique et de l'électronique, qui attirent tous les jeunes talents de la nouvelle économie. De plus Shenzhen est devenue aussi une « base arrière » pour de nombreux hongkongais.</p>
    <p><span class="red">Le + :</span> Shenzhen a vu s'implanter un nombre très important d'importateurs hongkongais, désireux de se développer sur la Chine continentale, ce qui en fait aussi une porte d'entrée pour Hong Kong.</p>
  </div>
  <div class="abs lead-txt" style="left:13px;top:497px;width:355px">Vineway Events a un bureau à Shenzhen, et a déjà organisé 2 événements majeurs qui ont attiré plus de 350 visiteurs professionnels.</div>
  <div class="foot-bar"></div>
</section>
<div class="page-label" style="left:626px;top:571px">PAGE 1</div>

<!-- PAGE 2 -->
<section class="page p-two">
  <div class="abs form-txt" style="left:13px;top:12px;width:230px">
    <b>LA FORMULE DE PARTICIPATION</b>
    <div class="bullet"><i></i>1 ville : 1 500 Eur</div>
    <div class="bullet"><i></i>2 villes : 2 500 Eur</div>
  </div>
  <div class="abs brand" style="left:325px;top:14px;flex-direction:column;gap:1px;font-size:5px"><span class="dot" style="width:16px;height:16px"></span>Vineway Events</div>
  <div class="abs form-txt" style="left:13px;top:44px;width:355px">
    <b>LES PRIX DE PARTICIPATION COMPRENNENT :</b>
    <div style="display:flex;gap:12px">
      <div style="flex:1">
        <div class="bullet"><i></i>Présentation catalogue (présentation en page 4), une page + logo,</div>
        <div class="bullet"><i></i>Une table avec nappe blanche, chevalet société, badge,</div>
      </div>
      <div style="flex:1">
        <div class="bullet"><i></i>2 seaux à glaces, un crachoir, une corbeille de pain ou crackers, petites bouteilles d'eau,</div>
        <div class="bullet"><i></i>L'envoi de 24 bouteilles en échantillons.</div>
      </div>
    </div>
    <div style="margin-top:6px"><b>N'EST PAS COMPRIS :</b></div>
    <div style="display:flex;gap:12px">
      <div style="flex:1" class="bullet"><i></i>Votre déplacement depuis la France et les vols intérieurs,</div>
      <div style="flex:1" class="bullet"><i></i>Votre hébergement.</div>
    </div>
  </div>
  <div class="abs reg-rule"></div>
  <div class="abs reg-box"><b>FICHE D'INSCRIPTION EXPOS ASIE 2017</b><span>A retourner par e-mail à <span class="red">inscription@vineway-events.net</span></span><span>Avant le 1er novembre 2017</span></div>
  <div class="abs" style="left:13px;top:160px;width:355px">
    <div class="dotrow">Entreprise :<span class="fill"></span></div>
    <div class="dotrow">Nom du Contact :<span class="fill"></span></div>
    <div class="dotrow">Adresse :<span class="fill"></span></div>
    <div class="dotrow">Tél. :<span class="fill"></span>E-mail :<span class="fill"></span></div>
    <div class="dotrow">Nom et Prénom de la ou des personne(s) faisant le déplacement :<span class="fill"></span></div>
    <div class="dotrow"><span class="fill"></span>Portable :<span class="fill"></span></div>
  </div>
  <div class="abs form-head" style="left:13px;top:220px">FORMULE</div>
  <div class="abs" style="left:13px;top:230px;width:355px">
    <table class="grid">
      <tr><td class="c">TAIPEI, le 5 décembre 2017<br>1,500 Eur</td><td class="c">SHENZHEN, le 7 décembre 2017<br>1,500 Eur</td></tr>
      <tr><td class="c" colspan="2">TAIPEI, le 5 décembre 2017 &amp; SHENZHEN, le 7 décembre 2017<br>2,500 Eur</td></tr>
    </table>
  </div>
  <div class="abs form-head" style="left:13px;top:275px">OPTIONS</div>
  <div class="abs" style="left:13px;top:285px;width:355px">
    <table class="grid">
      <tr><td style="width:90px"></td><td class="c" style="width:90px">04/12 - Taipei, Grand Plaza</td><td class="c" style="width:90px">06/12 - Shenzhen, Riverside</td><td></td></tr>
      <tr><td>Hébergement<br>• Une personne = 150 Eur/nuit<br>• Deux personnes = 165 Eur/nuit<br>(<span class="box"></span>double <span class="box"></span>twin)<br>• Extra-room</td>
        <td class="c"><br><span class="box"></span>OUI <span class="box"></span>NON<br><span class="box"></span>OUI <span class="box"></span>NON<br><br><span class="box"></span>OUI <span class="box"></span>NON</td>
        <td class="c"><br><span class="box"></span>OUI <span class="box"></span>NON<br><span class="box"></span>OUI <span class="box"></span>NON<br><br><span class="box"></span>OUI <span class="box"></span>NON</td><td></td></tr>
      <tr><td>Interprète (150 Eur/ville)</td><td class="c"><span class="box"></span>OUI <span class="box"></span>NON</td><td class="c"><span class="box"></span>OUI <span class="box"></span>NON</td><td></td></tr>
      <tr><td>Echantillons supplémentaires<br>24 bouteilles supplémentaires</td><td class="c"><span class="box"></span>OUI <span class="box"></span>NON</td><td class="c"><span class="box"></span>OUI <span class="box"></span>NON</td><td></td></tr>
      <tr><td></td><td></td><td class="c">TOTAL OPTIONS</td><td></td></tr>
    </table>
  </div>
  <div class="abs form-head" style="left:13px;top:418px">TOTAL FORMULE + OPTIONS RETENUES =</div>
  <div class="abs form-txt" style="left:13px;top:428px;width:355px;font-size:4.6px;line-height:6px">Votre inscription ne sera validée qu'à réception d'un premier règlement de 50% du montant total indiqué ci-dessus. Le solde devant être réglé au plus tard 15 jours avant, dans le cas contraire, l'accès vous sera refusé. <b>Paiement par transfert bancaire en Euro.</b></div>
  <div class="abs" style="left:13px;top:444px;width:355px">
    <table class="grid">
      <tr><td style="width:50%;line-height:7px">Bank Name: Harbour Bank Hong Kong<br>Swift Code : HRBKHKHHXXX<br>Bank address: 8 Harbour Avenue, Central, Hong Kong<br>Account name: VINEWAY EVENTS LTD</td>
        <td style="line-height:6px">Merci d'identifier votre transfert par "EWDT – votre société", et merci de ne déduire aucune charge bancaire liée au transfert, qui reste à votre charge.</td></tr>
      <tr><td colspan="2">Account No: 000-123456-789</td></tr>
    </table>
  </div>
  <div class="abs form-txt" style="left:13px;top:515px;font-size:4.6px">Règlement sur les conditions générales de vente sur demande à : <span class="red">inscription@vineway-events.net</span></div>
  <div class="foot-bar"></div>
</section>
<div class="page-label" style="left:193px;top:1163px">PAGE 2</div>

<!-- BACK COVER -->
<section class="page p-back">
  <div class="abs sheet">
    <div class="abs sheet-mark" aria-hidden="true"></div>
    <div class="abs sheet-title" style="left:0;right:0;top:10px">PRESENTATION POUR LE CARNET DE DEGUSTATION</div>
    <div class="fl" style="top:38px">RÉGION VITICOLE :<span class="fill"></span></div>
    <div class="fl" style="top:53px">SOCIÉTÉ SOUS LAQUELLE VOUS SOUHAITEZ APPARAITRE DANS LE CATALOGUE :<span class="fill"></span></div>
    <div class="fl" style="top:86px">NOM :<span class="fill"></span>PRÉNOM :<span class="fill"></span></div>
    <div class="fl" style="top:99px">FONCTION :<span class="fill" style="flex:.86"></span><span style="flex:1"></span></div>
    <div class="fl" style="top:111px">E-MAIL :<span class="fill"></span>SITE INTERNET :<span class="fill"></span></div>
    <div class="fl" style="top:126px">TEL :<span class="fill"></span>FAX :<span class="fill"></span></div>
    <div class="fl" style="top:160px">DESCRIPTION DE LA SOCIÉTÉ (VOS POINTS FORTS EN 4 LIGNES) :</div>
    <div class="fl" style="top:175px"><span class="fill"></span></div>
    <div class="fl" style="top:191px"><span class="fill"></span></div>
    <div class="fl" style="top:207px"><span class="fill"></span></div>
    <div class="fl" style="top:223px"><span class="fill"></span></div>
    <div class="fl" style="top:244px">LA SURFACE DU VIGNOBLE :<span class="fill"></span>HECTARES – PRODUCTION :<span class="fill"></span>HL OU<span class="fill"></span>BOUTEILLES (0,75 L).</div>
    <div class="fl" style="top:282px"><u>IMPORTATEUR :</u> AVEZ-VOUS UN OU PLUSIEURS IMPORTATEUR(S) SUR CE PAYS :<span style="flex:1"></span><span><span class="box"></span> OUT &nbsp;<span class="box"></span> NOT</span><span style="width:40px"></span></div>
    <div class="fl" style="top:300px">SOUHAITEZ-VOUS QU'ON LE MENTIONNE SUR LE CARNET DE DÉGUSTATION :<span style="flex:1"></span><span><span class="box"></span> OUT &nbsp;<span class="box"></span> NOT</span><span style="width:40px"></span></div>
    <div class="fl" style="top:326px">MERCI DE NOUS DONNER LE(S) NOM(S) ET COORDONNÉES<span class="fill"></span></div>
    <div class="fl" style="top:342px"><span class="fill"></span></div>
    <div class="sheet-title abs" style="left:0;right:0;top:365px;font-size:9px">MERCI D'ENVOYER VOTRE LOGO AVEC LA PRÉSENTATION</div>
    <div class="fl" style="top:394px">FAIT À :</div>
    <div class="fl" style="top:404px">LE :</div>
    <div class="fl" style="top:414px">PAR :</div>
    <div class="fl" style="top:432px">CACHET DE L'ENTREPRISE :<span style="flex:1"></span>SIGNATURE :<span style="width:55px"></span></div>
  </div>
  <div class="abs contact-head">POUR NOUS CONTACTER : VINEWAY EVENTS SHENZHEN</div>
  <div class="abs contact-pill">
    <b>LINA ZHOU :</b> &nbsp;&nbsp;
    <svg class="ico" width="5" height="5" viewBox="0 0 10 10"><path d="M2 1l2 2-1 1.5c.8 1.3 1.7 2.2 3 3L7.5 6l2 2-1.5 1.5C4.5 9 1 5.5.5 2.5z" fill="#fff"/></svg>+86 (0) 755 0000 1234 &nbsp;&nbsp;
    <svg class="ico" width="6" height="5" viewBox="0 0 12 9"><rect x=".5" y=".5" width="11" height="8" fill="none" stroke="#fff"/><path d="M.5.5L6 5l5.5-4.5" fill="none" stroke="#fff"/></svg><b>lzhou@vineway-events.net</b><br>
    <svg class="ico" width="4" height="6" viewBox="0 0 8 12"><path d="M4 0a4 4 0 0 1 4 4c0 3-4 8-4 8S0 7 0 4a4 4 0 0 1 4-4z" fill="#fff"/><circle cx="4" cy="4" r="1.5" fill="#e3101a"/></svg>Room 5, first floor, Harbour Building, 18 Bay Road, Nanshan district, Shenzhen, China
  </div>
</section>
<div class="page-label" style="left:626px;top:1163px">BACK COVER</div>

</body>
</html>
```